Security Camera Sign

14” high x 11” wide Color: Blue, Yellow, Black and white

Make the sign vertical
Replace red with blue
WARNING: Black over yellow
These premises are protected by Closed Circuit Television: On white
Images are recorded for crime prevention and public safety. Unauthorized access, theft or vandalism will result in prosecution: On Blue

Target Market(s)

Outdoor commercial building

Industry/Entity Type

Security

Requirements
Nice to have
• I would like the sign stand out. If you need more colors? Thanks Ok

```html
<!DOCTYPE html>
<html lang="en">
<head>
<meta charset="utf-8">
<title>Security Camera Sign</title>
<link rel="stylesheet" href="https://fonts.googleapis.com/css2?family=Anton&family=Arimo:wght@700&family=Roboto+Condensed:wght@700&display=swap">
<style>
  :root {
    --sign-yellow: #ffdf00;
    --sign-blue: #1f4fa8;
    --sign-black: #1b1b1b;
    --sign-white: #ffffff;
    --text-dark: #222222;
    --camera-light: #e6e8ea;
    --camera-mid: #b9bdc1;
    --camera-dark: #5c6064;
  }
  * { box-sizing: border-box; margin: 0; padding: 0; }
  html, body {
    width: 944px;
    height: 1200px;
    overflow: hidden;
    background: var(--sign-white);
  }
  .sign {
    position: absolute;
    left: 28px;
    top: 40px;
    width: 888px;
    height: 1130px;
    border: 7px solid var(--sign-black);
    border-radius: 58px;
    overflow: hidden;
    background: var(--sign-white);
  }
  .header {
    position: absolute;
    left: 0; top: 0;
    width: 100%;
    height: 308px;
    background: var(--sign-yellow);
  }
  .header-title {
    position: absolute;
    left: 0; right: 0;
    top: 60px;
    text-align: center;
    font-family: "Anton", "Impact", sans-serif;
    font-size: 178px;
    line-height: 1;
    letter-spacing: 2px;
    color: var(--sign-black);
    transform: scaleX(1.14);
    background: linear-gradient(180deg, #3a3a3a 0%, #111111 55%, #000000 100%);
    -webkit-background-clip: text;
    background-clip: text;
    -webkit-text-fill-color: transparent;
  }
  .hazard-stripe {
    position: absolute;
    left: 0;
    width: 100%;
    height: 27px;
    background: repeating-linear-gradient(
      -60deg,
      var(--sign-black) 0 20px,
      var(--sign-white) 20px 36px
    );
  }
  .hazard-stripe.top { top: 308px; }
  .hazard-stripe.bottom { top: 777px; }
  .camera-image {
    position: absolute;
    left: 455px;
    top: 350px;
    width: 405px;
    height: 410px;
    border-radius: 30px;
    background: radial-gradient(ellipse at 45% 35%, var(--camera-light) 0%, var(--camera-mid) 60%, var(--camera-dark) 100%);
  }
  .notice {
    position: absolute;
    left: 20px;
    top: 404px;
    width: 450px;
    text-align: center;
  }
  .notice-lead {
    font-family: "Arimo", "Helvetica", sans-serif;
    font-weight: 700;
    font-size: 51px;
    line-height: 63px;
    color: var(--text-dark);
  }
  .notice-system {
    margin-top: 17px;
    font-family: "Roboto Condensed", "Arial Narrow", sans-serif;
    font-weight: 700;
    font-size: 60px;
    line-height: 58px;
    color: var(--sign-blue);
    text-transform: uppercase;
  }
  .footer {
    position: absolute;
    left: 0;
    top: 804px;
    width: 100%;
    bottom: 0;
    background: var(--sign-blue);
  }
  .footer-text {
    position: absolute;
    left: 0; right: 0;
    top: 60px;
    text-align: center;
    font-family: "Arimo", "Helvetica", sans-serif;
    font-weight: 700;
    font-size: 45px;
    line-height: 54px;
    color: var(--sign-white);
  }
</style>
</head>
<body>
  <div class="sign">
    <header class="header">
      <h1 class="header-title">WARNING</h1>
    </header>
    <div class="hazard-stripe top"></div>

    <div class="camera-image" role="img" aria-label="Photograph of a white outdoor security camera on a wall bracket"></div>

    <div class="notice">
      <p class="notice-lead">These<br>premises are<br>protected by</p>
      <p class="notice-system">Closed Circuit<br>Television</p>
    </div>

    <div class="hazard-stripe bottom"></div>
    <footer class="footer">
      <p class="footer-text">Images are recorded for crime<br>prevention and public safety.<br>Unauthorized access, theft or<br>vandalism will result in prosecution</p>
    </footer>
  </div>
</body>
</html>
```